Create a premium soap bar box bar design for an all-natural, men's skincare brand.

We are launching a men’s premium, natural soap bar and skincare business. To start, we will be launching cold-press, all-natural soap bars with a few additional products such as lotions. We plan to expand our line into additional skincare products such as face exfoliants, moisturizers and cleansers that target basic needs such as anti-aging, clarifying and hydrating.

Our target audience is men ages 25-50, with a secondary audience of male teens. Our target audience are mid to high income, professionals that live in more urban areas, but enjoy being active outdoors after work and on the weekends. Our target audience are hard workers, humble and want to enjoy all that life has to offer – whether that’s on top of a mountain or an ocean wave. They hike, bike, skateboard, surf or any other sport that gets them outside. They are husbands, brothers and fathers – there for their family and friends.

Our brand is sophisticated, adventurous and has a sense of humor. Many of our competitors either focus on the rugged outdoors or are more pretentious. We are in-between. We are free spirited and love the fresh air. Our products are trustworthy with no toxic chemicals or harsh ingredients. We are all-natural and provide high-quality, premium products that our audience expects and deserves.

Target Market(s)

Men, ages 25-54 who are high-earning professionals, yet enjoy getting outdoors and being active on the weekends - hiking, biking, surfing, skateboarding and more.

Industry/Entity Type

Men's skincare

Font styles to use
Sans Serif

Requirements
Must have
• See attachments
Nice to have
• We would prefer to a have a premium, slightly more modern looking design that will appeal to our target audience and slightly higher price point.
Should not have
• Please do not include an icon for the fragrance, i.e. cinnamon sticks. However, we do need some differentiation for the fragrance, i.e. color, etc. as it will be on the shelf with other fragrances.

```html
<!DOCTYPE html>
<html lang="en">
<head>
<meta charset="utf-8">
<title>Ridgewell Cinnamon Bark Soap Box</title>
<link href="https://fonts.googleapis.com/css2?family=Nunito+Sans:wght@400;600;700;800&display=swap" rel="stylesheet">
<style>
  :root {
    --page: #f5f5f5;
    --kraft: #c7ae89;
    --kraft-light: #e8e0d2;
    --band-top: #2f4d6a;
    --band-mid: #24384e;
    --band-bottom: #1a1c21;
    --stripe: #c9a386;
    --ink-light: #ffffff;
    --label: #222222;
  }
  * { margin: 0; padding: 0; box-sizing: border-box; }
  html, body { width: 1200px; height: 1000px; overflow: hidden; background: var(--page); }
  body { position: relative; font-family: "Nunito Sans", sans-serif; }

  .panel {
    position: absolute; top: 300px; width: 455px; height: 475px;
    background: var(--kraft);
    box-shadow: 0 12px 30px rgba(0,0,0,0.15);
    overflow: hidden;
  }
  .panel--front { left: 95px; }
  .panel--rear { left: 680px; }

  .kraft-texture {
    position: absolute; inset: 0;
    background: radial-gradient(circle at 52% 55%, var(--kraft-light) 0%, #ddd2bf 48%, var(--kraft) 72%);
  }

  .stripe { position: absolute; top: 0; bottom: 0; width: 18px; background: var(--stripe); }
  .stripe--left { left: 115px; }
  .stripe--right { left: 340px; }

  .band {
    position: absolute; top: 0; bottom: 0; left: 133px; width: 207px;
    background: linear-gradient(180deg, var(--band-top) 0%, var(--band-mid) 45%, var(--band-bottom) 100%);
    color: var(--ink-light); text-align: center;
  }

  /* front */
  .brand-name {
    margin-top: 160px;
    font-weight: 700; font-size: 26px; letter-spacing: 0.5px;
  }
  .product-name {
    font-weight: 800; font-size: 24px; line-height: 1.15; margin-top: 48px; letter-spacing: 0.3px;
  }
  .product-type { font-weight: 600; font-size: 16px; margin-top: 10px; }
  .product-size { position: absolute; bottom: 45px; left: 0; right: 0; font-size: 17px; font-weight: 600; }

  /* rear */
  .rear-headline { font-weight: 800; font-size: 23px; line-height: 1.15; margin-top: 60px; }
  .rear-copy {
    font-size: 13px; line-height: 1.6; font-weight: 600; margin: 26px 18px 0;
  }
  .rear-copy strong { font-size: 16px; font-weight: 800; }
  .rear-link { font-size: 8px; font-weight: 600; margin-top: 20px; }
  .features { display: flex; justify-content: space-around; margin: 18px 6px 0; }
  .feature { width: 50px; font-size: 8px; line-height: 1.15; font-weight: 600; }
  .feature-badge {
    width: 22px; height: 22px; border-radius: 50%; background: var(--ink-light);
    margin: 0 auto 5px;
  }

  .view-label {
    position: absolute; top: 836px; width: 455px; text-align: center;
    font-family: "Nunito Sans", sans-serif; font-weight: 800; font-size: 12px; color: var(--label);
  }
  .view-label--front { left: 118px; }
  .view-label--rear { left: 703px; }
</style>
</head>
<body>
  <section class="panel panel--front">
    <div class="kraft-texture" role="img" aria-label="Kraft board with large faint decorative emblem"></div>
    <div class="stripe stripe--left"></div>
    <div class="stripe stripe--right"></div>
    <div class="band">
      <div class="brand-name">Ridgewell</div>
      <div class="product-name">CINNAMON<br>BARK</div>
      <div class="product-type">Men’s Natural Soap</div>
      <div class="product-size">5 Oz. Bar</div>
    </div>
  </section>

  <section class="panel panel--rear">
    <div class="kraft-texture" role="img" aria-label="Kraft board with large faint decorative emblem"></div>
    <div class="stripe stripe--left"></div>
    <div class="stripe stripe--right"></div>
    <div class="band">
      <h2 class="rear-headline">Real Ingredients<br>for Real Guys.</h2>
      <p class="rear-copy">Bring the outdoors in using real, natural ingredients on your skin. Traditional bar soap contains harsh chemical ingredients that can be harmful to you and the environment. Lather up with Ridgewell’s handcrafted, all-natural soap and <strong>feel the difference.</strong></p>
      <p class="rear-link">Check out all our products at ridgewell.com</p>
      <div class="features">
        <div class="feature"><div class="feature-badge"></div>Made in<br>USA</div>
        <div class="feature"><div class="feature-badge"></div>No harsh<br>chemicals</div>
        <div class="feature"><div class="feature-badge"></div>Sustainably<br>sourced</div>
        <div class="feature"><div class="feature-badge"></div>Hand-<br>crafted</div>
      </div>
    </div>
  </section>

  <div class="view-label view-label--front">FRONT VIEW</div>
  <div class="view-label view-label--rear">REAR VIEW</div>
</body>
</html>
```